Manufacturing company needs new business card.

I need a unique Business Card that will truly stand out. Nothing too busy. Simple is good, right? Not looking for a standard design either. No cookie cutter layout. I am just looking for something interesting and a bit different. Does't have to completely off the wall crazy, just not your run of the mill business card. Clean and modern with a touch of industrial.

Target Market(s)

Air conditioning industry, Architects, builders.

Industry/Entity Type

Business

Contact Information for Business Card

Details to be included on card are:

Peter Vance
Managing Director

T: 1300 847 519
M: 0428 593 174
W: www.brenvaleworks.com.au
E: peter.vance@brenvaleworks.com.au
A: 58 Harwick Lane, Sydney NSW 2000

Font styles to use
Sans Serif

Colors
0355a3
848484
fbfbfb

Requirements
Must have
• Card design must be landscape.

```html
<!DOCTYPE html>
<html lang="en">
<head>
<meta charset="utf-8">
<title>Brenvale Works – Business Card</title>
<link rel="stylesheet" href="https://fonts.googleapis.com/css2?family=Karla:wght@400;500;600;700&display=swap">
<style>
  :root {
    --brand-blue: #3157a4;
    --brand-grey: #848484;
    --card-white: #fbfbfb;
    --page-bg: #e9e9ea;
    --ink-dark: #2b2b2b;
  }
  * { box-sizing: border-box; margin: 0; padding: 0; }
  html, body {
    width: 1200px; height: 1200px; overflow: hidden;
    background: var(--page-bg);
    font-family: "Karla", Arial, sans-serif;
  }
  .canvas { position: relative; width: 1200px; height: 1200px; }

  .card {
    position: absolute;
    width: 780px; height: 470px;
    overflow: hidden;
    box-shadow: 0 6px 18px rgba(0,0,0,0.12);
  }

  /* Front */
  .card-front { left: 150px; top: 90px; background: var(--card-white); }
  .front-brand {
    position: absolute; left: 0; right: 0; top: 150px;
    display: flex; align-items: center; justify-content: center; gap: 22px;
  }
  .brand-square { width: 54px; height: 54px; background: var(--brand-blue); }
  .brand-name {
    font-size: 52px; font-weight: 600; color: var(--brand-blue);
    letter-spacing: -0.5px;
  }
  .front-band {
    position: absolute; left: 0; right: 0; bottom: 0; height: 118px;
    background: var(--brand-blue);
    display: flex; align-items: center; justify-content: center; gap: 12px;
    color: #fff; font-size: 25px; letter-spacing: 0.3px;
  }

  /* Back */
  .card-back { left: 270px; top: 640px; background: var(--brand-blue); color: #fff; }
  .back-brand {
    position: absolute; left: 58px; top: 60px;
    display: flex; align-items: center; gap: 14px;
  }
  .back-brand .brand-square { width: 34px; height: 34px; background: #fff; }
  .back-brand .brand-name { font-size: 30px; color: #fff; letter-spacing: 0; }

  .person {
    position: absolute; left: 120px; width: 250px; top: 210px;
    text-align: center;
  }
  .person-name { font-size: 35px; font-weight: 700; letter-spacing: 1px; }
  .person-title { font-size: 22px; margin-top: 6px; letter-spacing: 0.3px; }

  .divider {
    position: absolute; left: 390px; top: 196px;
    width: 2px; height: 120px; background: rgba(255,255,255,0.85);
  }

  .contact-list {
    position: absolute; left: 425px; top: 194px; list-style: none;
    font-size: 23px; line-height: 34px; letter-spacing: 0.4px;
  }
  .contact-list li { display: flex; align-items: flex-start; gap: 16px; }
  .contact-list svg { flex: none; margin-top: 8px; }

  .back-band {
    position: absolute; left: 0; right: 0; bottom: 0; height: 63px;
    background: var(--card-white); color: var(--ink-dark);
    display: flex; align-items: center; justify-content: center; gap: 12px;
    font-size: 23px; letter-spacing: 0.4px;
  }
</style>
</head>
<body>
<main class="canvas">

  <section class="card card-front" aria-label="Business card front">
    <div class="front-brand">
      <span class="brand-square"></span>
      <span class="brand-name">Brenvale Works</span>
    </div>
    <div class="front-band">
      <svg width="20" height="20" viewBox="0 0 20 20" aria-hidden="true" fill="none" stroke="#fff" stroke-width="1.5">
        <circle cx="10" cy="10" r="8.5"/>
        <ellipse cx="10" cy="10" rx="3.8" ry="8.5"/>
        <line x1="1.5" y1="10" x2="18.5" y2="10"/>
        <line x1="3" y1="5.5" x2="17" y2="5.5"/>
        <line x1="3" y1="14.5" x2="17" y2="14.5"/>
      </svg>
      <span class="website">www.brenvaleworks.com.au</span>
    </div>
  </section>

  <section class="card card-back" aria-label="Business card back">
    <div class="back-brand">
      <span class="brand-square"></span>
      <span class="brand-name">Brenvale Works</span>
    </div>

    <div class="person">
      <div class="person-name">Peter Vance</div>
      <div class="person-title">Managing Director</div>
    </div>

    <div class="divider"></div>

    <ul class="contact-list">
      <li>
        <svg width="18" height="18" viewBox="0 0 18 18" aria-hidden="true" fill="none" stroke="#fff" stroke-width="1.5">
          <circle cx="9" cy="9" r="8"/>
          <path d="M6.2 5.2l1.4-.3.8 1.9-.9.7c.5 1.1 1.3 1.9 2.4 2.4l.7-.9 1.9.8-.3 1.4c-3.4.2-6.2-2.6-6-6z" fill="#fff" stroke="none"/>
        </svg>
        <span>1300 847 519</span>
      </li>
      <li>
        <svg width="18" height="20" viewBox="0 0 18 20" aria-hidden="true" fill="none" stroke="#fff" stroke-width="1.6">
          <rect x="4" y="1" width="10" height="18" rx="1.5"/>
          <line x1="7.5" y1="16" x2="10.5" y2="16"/>
        </svg>
        <span>0428 593 174</span>
      </li>
      <li>
        <svg width="18" height="22" viewBox="0 0 18 22" aria-hidden="true">
          <path d="M9 1a7 7 0 0 1 7 7c0 5-7 13-7 13S2 13 2 8a7 7 0 0 1 7-7z" fill="#fff"/>
          <circle cx="9" cy="8" r="2.6" fill="var(--brand-blue)"/>
        </svg>
        <span>58 Harwick Lane<br>Sydney NSW 2000</span>
      </li>
    </ul>

    <div class="back-band">
      <svg width="20" height="15" viewBox="0 0 20 15" aria-hidden="true" fill="none" stroke="#2b2b2b" stroke-width="1.4">
        <rect x="1" y="1" width="18" height="13"/>
        <path d="M1 1l9 7 9-7M1 14l6.5-6M19 14l-6.5-6"/>
      </svg>
      <span class="email">peter.vance@brenvaleworks.com.au</span>
    </div>
  </section>

</main>
</body>
</html>
```